Marketing Agency Needs Fresh New Look

PebbleCraftHub.com is a Digital Marketing agency with locations in North Carolina and Florida. And, yes, we do custom Websites too. When we're designing for ourselves, we prefer to outsource because we typically get fresher perspectives from designers involved in the project. Which is why we're here today posting this Redesign project for our very own website.

Overall, we like our website look/feel....but don't LOVE it. We need our new site to be a bit fresher and more current using some of today's web design/development trends.

Some of the details: We want to use more current font styles and sizes (ideally, we use 3 different fonts including one "handwritten" or script font). We use the little nerdy scientist way too much throughout our website. We want to project a positive, friendly image to our customers....but we also want to be considered serious professionals in our industry(s). So, we would like to see a better mix of fun & friendly with professional & completely capable.

Here are two examples of our local competitors and websites that we think are very well done and include some of elements we're looking to see on our new site:

1) www.craftwombats.example = these guys do a great job at mixing their cartoony dinosaur with realism imagery. Very clean & professional website, but also cool and interesting how they carry through some of their branding and toony graphic elements. We like the use of big circles to highlight certain elements. We feel that this would play well for us too because we already use some of these big circles/bubbles in our bokeh background.

2) www.velquinpixel.example = these guys have the same kind of top to bottom layout with big chunks for each section. They come across as a little more "buttoned up" then craftwombats, but still friendly enough to make a small business owner feel comfortable.

There are a few elements that we consider part of our brand and that we want to continue to use in our new design. They are as follows:
1) The nerdy scientist dude....we have 50+ variations of this little guy in every file format you need. I'll try to upload the whole set....at the least, you'll have one or two examples.

2) The electric green bokeh background you see at the top of each page of our website.

3) And our logo of course which is included in uploads.

Please feel free to ask me any questions. We're really open to new and fresh ideas and creativity. So...let 'r rip!

```html
<!DOCTYPE html>
<html lang="en">
<head>
<meta charset="utf-8">
<title>PebbleCraftHub.com – Marketing Chemistry</title>
<link rel="stylesheet" href="https://fonts.googleapis.com/css2?family=Oswald:wght@400;600;700&family=Open+Sans:wght@400;600;700&display=swap">
<style>
:root{
  --green:#5cb82e;
  --green-dark:#3f8f1a;
  --green-light:#a6e04a;
  --red:#e2452b;
  --red-dark:#c8331c;
  --orange:#f07a1d;
  --ink:#333;
  --muted:#777;
  --grey-bg:#ececec;
  --footer:#262626;
  --footer-deep:#1a1a1a;
  --white:#fff;
}
*{box-sizing:border-box;margin:0;padding:0}
html,body{width:709px;height:1200px;overflow:hidden}
body{font-family:"Open Sans",Arial,sans-serif;color:var(--ink);background:var(--white);position:relative}
.site-header{position:absolute;top:0;left:0;width:709px;height:44px;background:var(--white);display:flex;align-items:center;justify-content:space-between;padding:0 26px 0 22px;z-index:2;box-shadow:0 1px 3px rgba(0,0,0,.15)}
.brand{display:flex;align-items:center;gap:6px;font-family:"Open Sans",sans-serif;font-weight:700;font-size:15px;color:var(--green-dark)}
.brand-dot{width:12px;height:12px;border-radius:50%;background:var(--green)}
.main-nav{display:flex;gap:14px}
.main-nav a{font-size:8px;font-weight:700;color:#555;text-decoration:none;letter-spacing:.3px}
.main-nav a.is-active{color:var(--green-dark)}
.hero{position:absolute;top:44px;left:0;width:709px;height:262px;background:radial-gradient(circle at 20% 30%,#c4f06a 0,rgba(196,240,106,0) 35%),radial-gradient(circle at 75% 60%,#9ee040 0,rgba(158,224,64,0) 40%),linear-gradient(160deg,#8fd63a,#4aa91e)}
.hero-title{position:absolute;left:70px;top:46px;font-family:"Oswald",sans-serif;font-weight:700;color:var(--white);font-size:46px;line-height:1;letter-spacing:1px}
.hero-sub{position:absolute;left:70px;top:100px;font-family:"Oswald",sans-serif;font-weight:600;color:var(--white);font-size:24px;letter-spacing:.5px}
.hero-text{position:absolute;left:70px;top:138px;width:320px;font-size:8px;line-height:1.55;color:var(--white)}
.hero-mascot{position:absolute;right:92px;top:4px;width:180px;height:252px;border-radius:90px 90px 10px 10px;background:linear-gradient(180deg,rgba(255,255,255,.55),rgba(255,255,255,.25))}
.services-band{position:absolute;top:306px;left:0;width:709px;height:118px;background:linear-gradient(180deg,var(--red),var(--red-dark));display:flex;justify-content:center;gap:46px;padding-top:0}
.service{width:90px;text-align:center;position:relative;top:-34px}
.service-icon{width:62px;height:62px;margin:0 auto;border-radius:50%;background:var(--red);border:4px solid var(--white);display:flex;align-items:center;justify-content:center}
.service-name{margin-top:8px;color:var(--white);font-size:11px;font-weight:600;line-height:1.2}
.about{position:absolute;top:446px;left:0;width:709px;height:340px}
.tabs{position:absolute;left:50px;top:20px;width:118px}
.tab{display:block;height:24px;margin-bottom:8px;font-size:10px;font-weight:700;padding:5px 10px;color:var(--white);background:var(--green)}
.tab.is-active{background:var(--white);color:var(--orange);border:1px solid var(--orange)}
.welcome{position:absolute;left:176px;top:10px;width:240px;height:300px;background:var(--white);border:1px solid #ddd;box-shadow:0 2px 6px rgba(0,0,0,.12);padding:14px 16px}
.welcome h2{font-size:12px;color:var(--ink);font-weight:700;margin-bottom:8px}
.welcome p{font-size:7.5px;line-height:1.55;color:var(--muted);margin-bottom:10px}
.welcome h3{font-size:12px;font-weight:700;color:var(--ink);line-height:1.3;margin-bottom:8px}
.btn{display:inline-block;font-size:8px;font-weight:700;color:var(--white);padding:5px 10px;border-radius:2px}
.btn-orange{background:var(--orange)}
.btn-red{background:var(--red)}
.query{position:absolute;left:446px;top:0;width:210px;height:320px}
.query-title{background:var(--green);color:var(--white);font-size:13px;font-weight:700;padding:6px 14px;width:150px}
.query-form{margin-top:8px;width:150px}
.field{height:18px;border:1px solid #ccc;margin-bottom:6px;font-size:7px;color:#999;padding:4px 6px}
.field.is-area{height:44px}
.query-mascot{position:absolute;right:0;top:56px;width:80px;height:240px;border-radius:40px 40px 8px 8px;background:linear-gradient(180deg,#e8f3dc,#cfd9c6)}
.query .btn{position:absolute;left:120px;top:296px}
.testimonial{position:absolute;top:800px;left:0;width:709px;height:120px;background:var(--grey-bg)}
.testimonial-photo{position:absolute;left:88px;top:20px;width:78px;height:78px;border-radius:50%;border:3px solid var(--white);background:linear-gradient(160deg,#8aa26c,#5d6d4a)}
.testimonial-body{position:absolute;left:190px;top:22px;width:440px}
.testimonial-name{font-size:8px;font-weight:700;color:var(--green-dark);margin-bottom:6px}
.testimonial-body p{font-size:7px;line-height:1.55;color:var(--muted);margin-bottom:5px}
.clients{position:absolute;top:940px;left:0;width:709px;height:80px;display:flex;align-items:center;justify-content:center;gap:30px}
.client-badge{width:86px;height:26px;background:#cfcfcf;border-radius:3px}
.site-footer{position:absolute;top:1030px;left:0;width:709px;height:148px;background:var(--footer);padding:18px 0 0 78px;display:flex;gap:40px}
.footer-col h4{font-size:8px;font-weight:700;color:var(--green-light);margin-bottom:6px}
.footer-col ul{list-style:none}
.footer-col li{font-size:7px;color:#bbb;line-height:1.65;padding-left:8px;position:relative}
.footer-col li::before{content:"";position:absolute;left:0;top:5px;width:3px;height:3px;background:var(--green)}
.footer-contact{margin-left:auto;margin-right:70px;width:120px}
.footer-contact .brand{font-size:12px;color:var(--green-light);margin-bottom:6px}
.footer-contact p{font-size:7px;color:#bbb;line-height:1.6}
.social{display:flex;gap:5px;margin-top:8px}
.social span{width:16px;height:16px;background:#3b6fb6;border-radius:2px}
.footer-bar{position:absolute;top:1178px;left:0;width:709px;height:22px;background:var(--footer-deep);display:flex;justify-content:space-between;align-items:center;padding:0 78px;font-size:6.5px;color:#888}
</style>
</head>
<body>
<header class="site-header">
  <div class="brand"><span class="brand-dot"></span>PebbleCraftHub</div>
  <nav class="main-nav">
    <a class="is-active" href="#">HOME</a><a href="#">WHO WE ARE</a><a href="#">WHAT WE DO</a><a href="#">HOW IT WORKS</a><a href="#">WHY CHOOSE US</a><a href="#">GET IN TOUCH</a>
  </nav>
</header>

<section class="hero">
  <h1 class="hero-title">WE CREATE</h1>
  <p class="hero-sub">MARKETING CHEMISTRY</p>
  <p class="hero-text">PebbleCraftHub combines strategic thinking, creative design, technical expertise and innovative marketing to help businesses become more successful online.</p>
  <div class="hero-mascot" role="img" aria-label="Cartoon scientist mascot holding a flask"></div>
</section>

<section class="services-band">
  <div class="service"><div class="service-icon"><svg width="26" height="26" viewBox="0 0 26 26" fill="none" stroke="#fff" stroke-width="2"><rect x="3" y="5" width="20" height="13" rx="1"/><path d="M9 22h8M13 18v4"/></svg></div><p class="service-name">Web Design &amp; Development</p></div>
  <div class="service"><div class="service-icon"><svg width="26" height="26" viewBox="0 0 26 26" fill="none" stroke="#fff" stroke-width="2"><path d="M13 23s-7-7-7-12a7 7 0 0 1 14 0c0 5-7 12-7 12z"/><circle cx="13" cy="11" r="2.5"/></svg></div><p class="service-name">Local Search Marketing</p></div>
  <div class="service"><div class="service-icon"><svg width="26" height="26" viewBox="0 0 26 26" fill="none" stroke="#fff" stroke-width="2"><circle cx="11" cy="11" r="6"/><path d="M15.5 15.5L22 22"/></svg></div><p class="service-name">Search Engine Optimization</p></div>
  <div class="service"><div class="service-icon"><svg width="26" height="26" viewBox="0 0 26 26" fill="none" stroke="#fff" stroke-width="2"><path d="M8 4v18M18 4v18M4 9h18M4 17h18"/></svg></div><p class="service-name">PPC Advertising</p></div>
  <div class="service"><div class="service-icon"><svg width="26" height="26" viewBox="0 0 26 26" fill="none" stroke="#fff" stroke-width="2"><rect x="8" y="3" width="10" height="20" rx="2"/><path d="M12 19h2"/></svg></div><p class="service-name">Mobile Marketing</p></div>
</section>

<section class="about">
  <div class="tabs">
    <span class="tab is-active">What We Are</span>
    <span class="tab">What We Do</span>
    <span class="tab">Why Choose</span>
  </div>
  <article class="welcome">
    <h2>Welcome to PebbleCraftHub!</h2>
    <p>PebbleCraftHub is a leader in Web Design and Internet Marketing services for local, regional and national businesses throughout the United States. With offices in North Carolina and Florida, our dynamic team of creative and tech-savvy professionals is ready to help your business grow no matter how big or small your target market.</p>
    <h3>We understand that marketing your business online can be time...</h3>
    <p>Here at PebbleCraftHub we make it easy, effective and affordable. We take the time to get acquainted with you and your business so that we can recommend the best plan.</p>
    <span class="btn btn-orange">Read More</span>
  </article>
  <aside class="query">
    <div class="query-title">Customer Query</div>
    <div class="query-form">
      <div class="field">Your Name</div>
      <div class="field">Email Address</div>
      <div class="field">Your Telephone No.</div>
      <div class="field">Your Website URL</div>
      <div class="field is-area">Your Message</div>
    </div>
    <div class="query-mascot" role="img" aria-label="Cartoon scientist mascot standing beside the form"></div>
    <span class="btn btn-red">Submit Now</span>
  </aside>
</section>

<section class="testimonial">
  <div class="testimonial-photo" role="img" aria-label="Portrait photo of the client"></div>
  <div class="testimonial-body">
    <p class="testimonial-name">Dana R – Harborline Home Repair, Raleigh, NC</p>
    <p>Here, at PebbleCraftHub, we make it easy, effective and affordable. We take the time to get acquainted with you and your business so that we can recommend the best online marketing plan for your success. Once you come on board we start working right away and keep you informed every step of the way.</p>
    <p>Once you come on board with PebbleCraftHub, we lay out the action plan and keep the results coming month after month.</p>
  </div>
</section>

<section class="clients" aria-label="Clients">
  <span class="client-badge"></span><span class="client-badge"></span><span class="client-badge"></span><span class="client-badge"></span><span class="client-badge"></span>
</section>

<footer class="site-footer">
  <div class="footer-col"><h4>QUICK LINKS</h4><ul><li>Home</li><li>Who We Are</li><li>Portfolio</li><li>Blog</li><li>Community</li><li>Shop</li><li>Contact Us</li></ul></div>
  <div class="footer-col"><h4>SERVICES</h4><ul><li>Local SEO</li><li>SEO</li><li>Analytics</li><li>Social Media</li><li>Conversion Optimization</li><li>Email Marketing</li><li>Web Design &amp; Development</li></ul></div>
  <div class="footer-col"><h4>CUSTOMER SUPPORT</h4><ul><li>Support Request</li><li>Monthly Reports</li><li>Helpful Forms</li><li>Client Area</li><li>Video Tutorials</li></ul></div>
  <div class="footer-contact">
    <div class="brand"><span class="brand-dot"></span>PebbleCraftHub</div>
    <p>hello@pebblecrafthub.example</p>
    <p>555-014-2290</p>
    <p>555-014-2291</p>
    <div class="social"><span></span><span></span><span></span><span></span></div>
  </div>
</footer>
<div class="footer-bar"><span>Terms &amp; Conditions</span><span>Copyright © 2014</span></div>
</body>
</html>
```